The Quiet Hour Safeguard Handbook

A book cover. The book will be marketed as a promotional item for financial advisors, financial planners, independent insurance agents, bankers, and any professional who views their role as guardian of their clients assets and helping them manage risk.

```html
<!DOCTYPE html>
<html lang="en">
<head>
<meta charset="utf-8">
<title>The Quiet Hour Safeguard Handbook — Book Cover</title>
<link href="https://fonts.googleapis.com/css2?family=Montserrat:wght@600;700;800&display=swap" rel="stylesheet">
<style>
  :root {
    --page: #ffffff;
    --cover-blue: #0b55a1;
    --accent-yellow: #f2c117;
    --text-white: #ffffff;
    --art-light: #b9d6f2;
    --art-mid: #7fa9dc;
  }
  * { margin: 0; padding: 0; box-sizing: border-box; }
  html, body {
    width: 1200px;
    height: 821px;
    overflow: hidden;
    background: var(--page);
  }
  .canvas {
    position: relative;
    width: 1200px;
    height: 821px;
  }
  .book-cover {
    position: absolute;
    left: 326px;
    top: 0;
    width: 547px;
    height: 821px;
    background: var(--cover-blue);
    font-family: "Montserrat", Arial, sans-serif;
    color: var(--text-white);
    overflow: hidden;
  }
  .top-rule {
    position: absolute;
    left: 53px;
    top: 0;
    width: 4px;
    height: 70px;
    background: var(--accent-yellow);
  }
  .side-rule {
    position: absolute;
    left: 53px;
    top: 374px;
    width: 4px;
    height: 346px;
    background: var(--accent-yellow);
  }
  .title {
    position: absolute;
    left: 48px;
    top: 84px;
    font-weight: 800;
    font-size: 58px;
    line-height: 54px;
    letter-spacing: -0.5px;
    text-transform: uppercase;
  }
  .title span { display: block; }
  .title .title-highlight { color: var(--accent-yellow); }
  .subtitle {
    position: absolute;
    left: 69px;
    top: 372px;
    width: 170px;
    font-weight: 600;
    font-size: 19px;
    line-height: 22px;
    color: var(--accent-yellow);
  }
  .cover-art {
    position: absolute;
    left: 247px;
    top: 344px;
    width: 252px;
    height: 262px;
  }
  .tagline {
    position: absolute;
    left: 78px;
    top: 642px;
    font-weight: 700;
    font-size: 17.5px;
    line-height: 21px;
    text-transform: uppercase;
    letter-spacing: 0.1px;
  }
  .author {
    position: absolute;
    left: 49px;
    top: 728px;
    font-weight: 800;
    font-size: 47px;
    line-height: 56px;
    letter-spacing: -0.3px;
  }
</style>
</head>
<body>
  <main class="canvas">
    <section class="book-cover">
      <div class="top-rule"></div>
      <h1 class="title">
        <span>The</span>
        <span class="title-highlight">Quiet Hour</span>
        <span>Safeguard</span>
        <span>Handbook</span>
      </h1>
      <div class="side-rule"></div>
      <p class="subtitle">Protect yourself and family in the AI age</p>
      <svg class="cover-art" role="img" aria-label="Illustration of a businessman standing beside a large light bulb and a gold dollar coin" viewBox="0 0 252 262">
        <defs>
          <linearGradient id="artTone" x1="0" y1="0" x2="1" y2="1">
            <stop offset="0" stop-color="var(--art-light)"/>
            <stop offset="1" stop-color="var(--art-mid)"/>
          </linearGradient>
        </defs>
        <rect x="0" y="0" width="252" height="262" rx="6" fill="url(#artTone)"/>
      </svg>
      <p class="tagline">It’s better to have it and not need it<br>than need it and not have it.</p>
      <p class="author">Jack Renwick</p>
    </section>
  </main>
</body>
</html>
```